Dấu Lặng Sương Mai (The Lantern Of Quiet Evening Rivers)

The purpose of this project is to share the Lotari Craft technique of Spiritual Meditation. The technique is originally in the Vietnamese language and need to share worldwide in other languages.

Spiritual Meditation through Lotari Craft meditation method to assist mind traveling through body to eternity. This method of meditation has many techniques and different purpose of all levels of understanding of mind, the more understanding the more explored the ability self esteem, self conscious, self determination to search for eternity. It’s not all could practice, it’s depending the previous life’s experiences that’s existing in their own mind. Because when a human life was born that never know their mind history came from. All human life has been programmed by almighty gods or the gods of living universe.

Heaven, Earth, Human were all connected through minds not though the body, the body could not reach to heaven.

Only mind could reach to Heaven because almighty gods design them. All life’s on earth are controlled by almighty though mind.

***UPDATED GUIDE FOR DESIGNERS:

1/. Theme page: I wish to have my own theme as a background to be supplied [p1: Theme]
(a) Use the logo provided [p2] and add the words on the bottom "Thiên Địa Nhân" If the designers
are foreign languages then they use alphabetical characters throughout the design.
(b). In the existing site (minhsuong.org) has a picture [p3] of the author of the book which has 4 words
"Dấu Lặng Sương Mai" I want to have it on my theme page in a similar dimension.
(c). I like to add a picture [p4] of a white flower on the right-hand side of the theme to balance with
the right side.
(d) At the bottom of the theme
(i) Write the words "Welcome To minhsuong.org" and the next line down
(ii). Write the words "Tu Thiền Lối Xanh Mộc An Nguyên Sơn Thủy Đình Viên"

2/. Menu:
(a). Introduction: Trang Chủ "Lời Giới Thiệu"
(b). Author story: Tiểu Sử
(c). Books "The Lantern of quiet evening rivers" Kinh Sách "Dấu Lặng Sương Mai"
(i) Book 1
(ii) Book 2
(iii) Book 3
(iv) Book 4
(v) Book 5
(vi) Book 6 to be continued..
(d). Method for beginners: Phương pháp Thiền cho 6 tháng đầu cho hành giả mới tham gia
(e) Method for Practitioners: Thiền Thực Hành Theo Lối Xanh Mộc An Nguyên Sơn Thủy Đình
Viên
(f) Register/Login: Đăng nhập
(g). Contact: Liên hệ

The following is my attached content to support the information

Sick

Target Market(s)

Body and Mind

Industry/Entity Type

Spiritual Meditaion

Coding

Coded - Design and coding required

Number of Pages Required

5+ page

Font styles to use
Sans Serif

Requirements
Must have
• Clearly presented the author of books and audio
Nice to have
• The author wish to introduce her books which were written through her spiritual meditaion she wish to share to all mankind
Should not have
• Advertise, other religious contain...

```html
<!DOCTYPE html>
<html lang="en">
<head>
<meta charset="utf-8">
<title>Method for Beginners</title>
<link rel="stylesheet" href="https://fonts.googleapis.com/css2?family=Quicksand:wght@500;600&family=Crimson+Text&display=swap">
<style>
  :root {
    --page-bg: #f5f7fa;
    --nav-bg: #f6f7f9;
    --ink: #3a3a3a;
    --nav-ink: #4a4a4a;
    --accent: #ff9f55;
    --card-start: #ffb76c;
    --card-end: #ff9a55;
    --white: #ffffff;
    --photo-deep: #2f6e6f;
    --photo-mid: #5fa3a3;
    --petal: #eef2ea;
  }
  * { box-sizing: border-box; margin: 0; padding: 0; }
  html, body { width: 1200px; height: 574px; overflow: hidden; }
  body { background: var(--page-bg); font-family: "Quicksand", sans-serif; position: relative; }

  .site-header {
    position: absolute; left: 20px; top: 0; width: 1158px; height: 50px;
    background: var(--nav-bg); box-shadow: 0 2px 6px rgba(0,0,0,.12);
  }
  .brand {
    position: absolute; left: 14px; top: 0; height: 50px;
    display: flex; align-items: center; gap: 6px;
    font-size: 12px; font-weight: 600; color: var(--accent);
  }
  .brand-dot { width: 14px; height: 14px; border-radius: 50%; background: var(--accent); }
  .main-nav {
    position: absolute; right: 22px; top: 0; height: 50px;
    display: flex; align-items: center; gap: 26px;
  }
  .main-nav a {
    position: relative; font-size: 11.3px; font-weight: 500;
    color: var(--nav-ink); text-decoration: none; white-space: nowrap;
  }
  .main-nav a.is-active { color: var(--accent); }
  .main-nav a.is-active::after {
    content: ""; position: absolute; left: -6px; right: -6px; top: 21px;
    height: 2px; background: var(--accent); border-radius: 1px;
  }

  .blossom-art {
    position: absolute; left: 91px; top: 50px; width: 375px; height: 259px;
    background: radial-gradient(ellipse at 25% 55%, rgba(90,167,230,.35), rgba(90,167,230,0) 60%),
                radial-gradient(ellipse at 60% 25%, rgba(60,60,60,.12), rgba(60,60,60,0) 55%);
  }
  .section-mark {
    position: absolute; left: 592px; top: 108px; width: 16px; height: 10px;
    border-radius: 8px 8px 3px 3px; background: #9fd0ee;
  }
  .section-title {
    position: absolute; left: 0; width: 1200px; top: 122px; text-align: center;
    font-size: 30px; font-weight: 500; color: var(--ink); letter-spacing: .2px;
  }

  .class-photo {
    position: absolute; left: 228px; top: 193px; width: 610px; height: 343px;
    background: radial-gradient(ellipse at 30% 55%, var(--petal) 0 18%, rgba(238,242,234,0) 30%),
                linear-gradient(135deg, var(--photo-deep), var(--photo-mid) 55%, var(--photo-deep));
  }
  .class-card {
    position: absolute; left: 547px; top: 279px; width: 416px; height: 267px;
    background: linear-gradient(135deg, var(--card-start), var(--card-end));
    padding: 42px 52px 0 52px; color: var(--white);
  }
  .class-card h2 { font-size: 22px; font-weight: 500; line-height: 1; margin-bottom: 20px; }
  .class-card p {
    font-family: "Crimson Text", serif; font-size: 12.6px; line-height: 19.5px; width: 312px;
  }
  .read-more {
    display: inline-flex; align-items: center; justify-content: center;
    margin-top: 24px; width: 117px; height: 34px; background: var(--white);
    color: var(--ink); font-size: 11px; font-weight: 500; text-decoration: none; border-radius: 2px;
  }
</style>
</head>
<body>
  <header class="site-header">
    <div class="brand"><span class="brand-dot"></span>Dấu Lặng Sương Mai</div>
    <nav class="main-nav">
      <a href="#" class="is-active">Introduction</a>
      <a href="#">Author Story</a>
      <a href="#">Books</a>
      <a href="#">Beginners</a>
      <a href="#">Practitioners</a>
      <a href="#">Login</a>
      <a href="#">Contact</a>
    </nav>
  </header>

  <div class="blossom-art" role="img" aria-label="Ink painting of a branch with blue blossoms"></div>

  <div class="section-mark" role="img" aria-label="Small lotus ornament"></div>
  <h1 class="section-title">Method for Beginners</h1>

  <div class="class-photo" role="img" aria-label="Photo of a white lotus flower among teal leaves"></div>

  <article class="class-card">
    <h2>First Six Months</h2>
    <p>Guiding new practitioners through the first six months of Lotari Craft meditation. Calm breathing, quiet sitting and gentle study help the mind travel through the body, step by step, toward inner peace.</p>
    <a href="#" class="read-more">Read More</a>
  </article>
</body>
</html>
```